Hair Extension Packaging

Update 2/16 - please keep submissions coming, I have no front runners yet. Thanks.

I need some new packaging designed for hair extensions. I have enclose pictures of what other companies packaging looks like and a few pictures of some inspiration. I am looking for a packaging that will appeal to a 20's-30's year old demographic and I like things along the lines of glamor/lace/vintage/boudoir/damask inspired. I am going to leave colors up to your creativity for the sample artwork and ask for changes if needed. Id like the design to be a standout but not loud.

The working name for this hair is "Velvetta"
Additional Text that I would like on the packaging "100% Premium Virgin Remy Human Hair"

Please keep in mind that the background of the packaging will have many different colors laying over it so be mindful of what the color you chose can effect the hair color in the packaging - no red or orange which can make the hair appear very warm and clash with ashy colors.

Working dimensions for the sample are 22" long, 3" wide.

****Once I decide on the front of the packaging I will also need the back designed which will consist of similar design as the front but with hair care instructions printed on it.***** This finished product must include front and back artwork, open Photoshop files, and additional bleed room for printing. I don't want to waste anyone's time so once I get a front design I like I will work with that artist to create the back.

Please message me with any questions.
Updates

Project Deadline Extended
Reason: Finalizing final choices. Thanks for your submissions!

Target Market(s)

Women in there 20"s - 30's. High fashion, luxurious, glamour

Industry/Entity Type

Hair

Font styles to use
Serif
Script

Requirements
Must have
• Id love the product name to be in script and then mixed with regular font (see the makeup logo example I enclosed)
Should not have
• Should not be masculine. Forget the blue and green colors

```html
<!DOCTYPE html>
<html lang="en">
<head>
<meta charset="utf-8">
<title>Velvetta – Hair Extension Packaging</title>
<link rel="stylesheet" href="https://fonts.googleapis.com/css2?family=Great+Vibes&family=Playfair+Display:ital,wght@1,400&display=swap">
<style>
  :root {
    --panel-plum: #3d2140;
    --panel-edge: #24122a;
    --champagne: #ecd3a4;
    --ivory: #fbf6ee;
    --window-plum: #6b3f6e;
    --window-mauve: #b792b4;
    --window-pearl: #f6eff4;
    --window-taupe: #a8949f;
    --tab-top: #5a3560;
    --tab-bottom: #ffffff;
  }
  * { margin: 0; padding: 0; box-sizing: border-box; }
  html, body {
    width: 1200px;
    height: 3188px;
    overflow: hidden;
    background: #ffffff;
  }
  .package {
    position: relative;
    width: 1200px;
    height: 3188px;
  }
  .front-panel {
    position: absolute;
    left: 0;
    top: 0;
    width: 1200px;
    height: 2073px;
    background: var(--panel-plum);
    border: 3px solid var(--panel-edge);
  }
  .brand-name {
    position: absolute;
    left: 0;
    top: 230px;
    width: 100%;
    height: 250px;
    text-align: center;
    font-family: "Great Vibes", cursive;
    font-weight: 400;
    font-size: 240px;
    line-height: 250px;
    color: var(--champagne);
  }
  .tagline {
    position: absolute;
    left: 0;
    top: 486px;
    width: 100%;
    text-align: center;
    font-family: "Playfair Display", serif;
    font-style: italic;
    font-weight: 400;
    font-size: 44px;
    line-height: 1;
    letter-spacing: 1px;
    color: var(--ivory);
  }
  .hair-window {
    position: absolute;
    left: 101px;
    top: 589px;
    width: 993px;
    height: 1381px;
    background: linear-gradient(to right,
      var(--window-plum) 0%,
      var(--window-mauve) 25%,
      var(--window-pearl) 51%,
      var(--window-taupe) 75%,
      var(--panel-plum) 100%);
  }
  .hanging-tab {
    position: absolute;
    left: 48px;
    top: 2073px;
    width: 1104px;
    height: 1115px;
    background: linear-gradient(to bottom, var(--tab-top) 0%, var(--tab-bottom) 100%);
  }
</style>
</head>
<body>
  <main class="package">
    <section class="front-panel">
      <h1 class="brand-name">Velvetta</h1>
      <p class="tagline">100% Premium Virgin Remy Human Hair</p>
      <div class="hair-window" role="img" aria-label="Clear window showing the hair extension bundle"></div>
    </section>
    <div class="hanging-tab"></div>
  </main>
</body>
</html>
```